Mailer Postcard for Potential Bankruptcy Clients

The postcard will be printed at 8.5"x6" to abide by the specification at the following link: https://www.mailtrelbo.com/submitting-art/specs/. I want an attractive two sided post card that includes my logo (see attachment). The design would have to have room for the website address, phone number, two location addresses and give them information about a civil action pending against them (You are being sued in X county (case# xxyx). We can help.). I don't really like the visuals of the attached postcard, so please use as a general guide for what I am trying to do. Ultimately, I want an ad that gets people to call me so I can help them.

I also want it to be compatible with the website (LoanHarbor.Legal).

Target Market(s)

Potential bankruptcy clients.

Industry/Entity Type

Legal

Colors

Designer to choose colors to be used in the design.

Requirements
Must have
• Phone number, addresses, website, and place for text regarding pending legal action against the receiver. Should say something to the effect: You have a pending legal action in (county name) County (court name [superior, magistrate, ect.]). Let us help you deal with it responsibly.
• Please note the design specifications at this link:

```html
<!DOCTYPE html>
<html lang="en">
<head>
<meta charset="utf-8">
<title>Loan Harbor Law Group – Mailer Postcard</title>
<link href="https://fonts.googleapis.com/css2?family=Fira+Sans:wght@400;500;600&family=Alegreya+Sans:wght@400;500&display=swap" rel="stylesheet">
<style>
  :root{
    --green:#37b98b;
    --green-soft:#7cc79a;
    --charcoal:#363636;
    --ink:#3b3b3b;
    --orange:#f5a623;
    --white:#ffffff;
    --page:#e9e9e9;
    --photo-a:#e6ecef;
    --photo-b:#b9c4cc;
  }
  *{box-sizing:border-box;margin:0;padding:0}
  html,body{width:935px;height:1200px;overflow:hidden}
  body{background:var(--page);position:relative;font-family:"Fira Sans",sans-serif;color:var(--ink)}
  .card{position:absolute;left:80px;width:807px;background:var(--white);overflow:hidden;box-shadow:0 2px 6px rgba(0,0,0,.18)}
  .card-front{top:42px;height:525px}
  .card-back{top:610px;height:520px}
  .card svg.shapes{position:absolute;inset:0}
  .abs{position:absolute}

  .brand{position:absolute;color:var(--ink);font-family:"Fira Sans",sans-serif;font-weight:500;line-height:1}
  .brand-name{display:block;font-size:38px;letter-spacing:-.5px}
  .brand-sub{display:block;font-size:15px;letter-spacing:3px;margin-top:8px}
  .brand-attorney{position:absolute;font-family:"Alegreya Sans",sans-serif;font-size:14px;color:var(--green-soft)}

  .notice{left:30px;top:300px;width:345px;text-align:center;color:var(--orange);font-size:16px;line-height:22px}
  .notice-call{margin-top:18px;font-weight:600;font-size:14px}
  .contact-band{left:0;top:456px;width:470px;height:40px;display:flex;align-items:center;gap:26px;padding-left:28px;color:var(--white)}
  .contact-item{display:flex;align-items:center;gap:8px}
  .contact-web{font-size:15px}
  .contact-phone{font-size:21px;font-weight:600}

  .section-title{color:var(--orange);font-weight:600;font-size:17px;letter-spacing:.3px}
  .about{left:40px;top:16px;width:470px}
  .about p{margin-top:6px;color:var(--white);font-family:"Alegreya Sans",sans-serif;font-size:13.6px;line-height:15.8px}
  .services{left:40px;top:176px}
  .services ul{list-style:none;margin-top:8px}
  .services li{display:flex;align-items:center;gap:9px;color:var(--white);font-family:"Alegreya Sans",sans-serif;font-size:13.5px;height:22.4px}
  .services li::before{content:"";width:8px;height:8px;border-radius:50%;background:var(--orange)}
  .stamp-box{left:655px;top:34px;width:96px;height:96px;border:1px solid #9a9a9a}
  .offices{left:573px;top:412px;font-size:9.5px;line-height:12px;color:var(--ink)}
  .office{display:flex;gap:7px;margin-bottom:5px}
  .office svg{flex:none;margin-top:1px}
  .back-contact{left:573px;top:462px;display:flex;gap:20px;font-size:11.5px;font-weight:500;color:var(--ink)}
</style>
</head>
<body>

<!-- Front -->
<section class="card card-front">
  <svg class="shapes" width="807" height="525" viewBox="0 0 807 525">
    <path d="M0,188 C150,260 330,260 430,225 C530,190 640,120 807,94 L807,525 L0,525 Z" fill="var(--charcoal)"/>
    <path d="M0,178 C150,250 330,250 430,215 C530,180 660,100 807,82" fill="none" stroke="var(--green)" stroke-width="8"/>
    <rect x="0" y="456" width="470" height="40" fill="var(--green)"/>
    <defs>
      <linearGradient id="photoTone" x1="0" y1="0" x2="1" y2="1">
        <stop offset="0" stop-color="var(--photo-a)"/>
        <stop offset="1" stop-color="var(--photo-b)"/>
      </linearGradient>
    </defs>
    <path role="img" aria-label="Photo: a smiling couple shaking hands with an attorney across a desk" d="M807,92 C680,110 520,170 460,270 C420,350 412,450 440,525 L807,525 Z" fill="url(#photoTone)"/>
    <path d="M807,92 C680,110 520,170 460,270 C420,350 412,450 440,525" fill="none" stroke="var(--white)" stroke-width="6"/>
    <path d="M807,85 C674,103 512,164 452,266 C411,348 403,450 431,525" fill="none" stroke="var(--green)" stroke-width="6"/>
  </svg>

  <div class="brand" style="left:40px;top:80px">
    <span class="brand-name">Loan Harbor</span>
    <span class="brand-sub">LAW GROUP</span>
  </div>
  <span class="brand-attorney" style="left:236px;top:150px">by Attorney M. Calloway</span>

  <div class="abs notice">
    <p>YOU HAVE A PENDING LEGAL ACTION IN (county name) COUNTY (court name [superior, magistrate, ect.]).</p>
    <p class="notice-call">LET US HELP YOU DEAL WITH IT RESPONSIBLY.</p>
  </div>

  <div class="abs contact-band">
    <span class="contact-item contact-web">
      <svg width="16" height="16" viewBox="0 0 16 16"><circle cx="8" cy="8" r="7" fill="none" stroke="#fff" stroke-width="1.6"/><path d="M1,8 H15 M8,1 C4,5 4,11 8,15 M8,1 C12,5 12,11 8,15" fill="none" stroke="#fff" stroke-width="1.3"/></svg>
      loanharbor.legal
    </span>
    <span class="contact-item contact-phone">
      <svg width="11" height="18" viewBox="0 0 11 18"><rect x="1" y="1" width="9" height="16" rx="2" fill="none" stroke="#fff" stroke-width="1.6"/><rect x="3" y="4" width="5" height="7" fill="#fff"/></svg>
      (404) 555-0137
    </span>
  </div>
</section>

<!-- Back -->
<section class="card card-back">
  <svg class="shapes" width="807" height="520" viewBox="0 0 807 520">
    <path d="M0,0 L548,0 C600,140 540,250 380,310 C270,350 140,358 0,356 Z" fill="var(--charcoal)"/>
    <path d="M556,0 C610,144 550,258 386,319 C274,360 142,367 0,365" fill="none" stroke="var(--white)" stroke-width="4"/>
    <path d="M568,0 C622,148 560,266 390,329 C278,370 144,377 0,375" fill="none" stroke="var(--green)" stroke-width="9"/>
    <rect x="0" y="500" width="807" height="10" fill="var(--green)"/>
  </svg>

  <div class="abs about">
    <h2 class="section-title">WHO ARE WE?</h2>
    <p>We are a Georgia Law Firm that is dedicated to being a one-stop shop for all debt woes that Georgians face. We are experienced bankruptcy attorneys that understand that people need more than just a bankruptcy lawyer. People need someone that is experienced in handling all of the practical aspects of avoiding bankruptcy, recovering from bankruptcy quickly, tackling stubborn student loans, and punishing abusive debt collectors when they violate the law. If you came to this website and have read this far, you should contact us to see if we can help you.</p>
  </div>

  <div class="abs services">
    <h2 class="section-title">OUR SERVICES</h2>
    <ul>
      <li>Mortgage Loan Modifications</li>
      <li>Credit Report Inaccuracies &amp; Errors</li>
      <li>Student Loans</li>
      <li>Debt Collection Violations</li>
      <li>Bankruptcy</li>
      <li>Free Credit Rebuilding Program</li>
    </ul>
  </div>

  <div class="abs stamp-box"></div>

  <div class="brand" style="left:48px;top:398px">
    <span class="brand-name" style="font-size:32px">Loan Harbor</span>
    <span class="brand-sub" style="font-size:13px;margin-top:7px">LAW GROUP</span>
  </div>
  <span class="brand-attorney" style="left:198px;top:456px;font-size:12px">by Attorney M. Calloway</span>

  <div class="abs offices">
    <div class="office">
      <svg width="8" height="11" viewBox="0 0 8 11"><path d="M4,0 C6.2,0 8,1.8 8,4 C8,6.5 4,11 4,11 C4,11 0,6.5 0,4 C0,1.8 1.8,0 4,0 Z" fill="var(--ink)"/><circle cx="4" cy="4" r="1.5" fill="#fff"/></svg>
      <span>4120 Elm Ridge Rd., Douglasville, Georgia 30134</span>
    </div>
    <div class="office">
      <svg width="8" height="11" viewBox="0 0 8 11"><path d="M4,0 C6.2,0 8,1.8 8,4 C8,6.5 4,11 4,11 C4,11 0,6.5 0,4 C0,1.8 1.8,0 4,0 Z" fill="var(--ink)"/><circle cx="4" cy="4" r="1.5" fill="#fff"/></svg>
      <span>515 Maple Crest Ave., NW Suite #1800 Atlanta,<br>Georgia 30303</span>
    </div>
  </div>

  <div class="abs back-contact">
    <span class="contact-item" style="gap:5px">
      <svg width="11" height="11" viewBox="0 0 16 16"><circle cx="8" cy="8" r="7" fill="none" stroke="var(--ink)" stroke-width="1.8"/><path d="M1,8 H15 M8,1 C4,5 4,11 8,15 M8,1 C12,5 12,11 8,15" fill="none" stroke="var(--ink)" stroke-width="1.5"/></svg>
      loanharbor.legal
    </span>
    <span class="contact-item" style="gap:5px;font-weight:600">
      <svg width="8" height="12" viewBox="0 0 11 18"><rect x="0" y="0" width="11" height="18" rx="2" fill="var(--ink)"/><rect x="3" y="3" width="5" height="8" fill="#fff"/></svg>
      (404) 555-0137
    </span>
  </div>
</section>

</body>
</html>
```